Business Card Design

We are a new company that grows and processes olives. We will be producing both olive oil and table olives. We will add grapes and wine making in about five years and hope to start a small restaurant with an observation window overlooking our olive processing area.
The design we have in mind is one that could be adapted to bottle lables for our olive products. Our thoughts are an oval design showing a night time view of a bay with a family of wolves resting on the shore. We would like a border on top of olive branches with olives. We are pretty open on the rest.

Industry/Entity Type

Restaurant

Contact Information for Business Card

Heron Creek Groves
31857 CR 46
Pinecrest, AL 36541
Dale Huston and Annelise Vogt

```html
<!DOCTYPE html>
<html lang="en">
<head>
<meta charset="utf-8">
<title>Heron Creek Groves – Business Card</title>
<link href="https://fonts.googleapis.com/css2?family=Arimo:wght@400;700&display=swap" rel="stylesheet">
<style>
  :root {
    --page-bg: #f1f1f1;
    --olive: #7b9a4c;
    --olive-deep: #4f7a3a;
    --card-black: #050505;
    --swoosh-white: #f4f4f4;
    --text-white: #f2f2f2;
    --mark-ink: #111111;
    --night-light: #3f6a35;
    --night-dark: #0b1a0b;
  }
  html, body {
    margin: 0;
    width: 1200px;
    height: 900px;
    overflow: hidden;
    background: var(--page-bg);
    font-family: "Arimo", Arial, sans-serif;
  }
  .business-card {
    position: absolute;
    left: 100px;
    top: 165px;
    width: 1000px;
    height: 570px;
    border-radius: 42px;
    overflow: hidden;
    box-shadow: 0 18px 40px rgba(0,0,0,0.18);
  }
  .card-background {
    position: absolute;
    inset: 0;
    width: 100%;
    height: 100%;
  }
  .brand-block {
    position: absolute;
    left: 55px;
    top: 70px;
    width: 360px;
    text-align: center;
  }
  .brand-scene {
    display: block;
    width: 330px;
    height: 330px;
    margin: 0 auto;
    border-radius: 50%;
    background: radial-gradient(circle at 45% 55%, var(--night-light) 0%, #1f3a1c 45%, var(--night-dark) 100%);
  }
  .brand-name {
    margin: 22px 0 0;
    font-weight: 700;
    font-size: 34px;
    color: var(--mark-ink);
  }
  .owners {
    position: absolute;
    left: 590px;
    top: 108px;
    width: 360px;
    text-align: center;
    color: var(--olive);
    font-size: 32px;
    line-height: 46px;
  }
  .owners p { margin: 0; }
  .contact-list {
    position: absolute;
    left: 606px;
    top: 300px;
    margin: 0;
    padding: 0;
    list-style: none;
    color: var(--text-white);
    font-size: 24px;
    line-height: 36px;
  }
  .contact-item {
    display: flex;
    align-items: flex-start;
  }
  .contact-icon {
    width: 26px;
    height: 26px;
    margin: 5px 12px 0 0;
    flex: none;
    fill: var(--olive);
  }
  .address-lines span { display: block; }
</style>
</head>
<body>
  <div class="business-card">
    <svg class="card-background" viewBox="0 0 1000 570" preserveAspectRatio="none" aria-hidden="true">
      <defs>
        <linearGradient id="silver" x1="0" y1="0" x2="1" y2="1">
          <stop offset="0" stop-color="#d6d6d6"/>
          <stop offset="0.6" stop-color="#b4b4b4"/>
          <stop offset="1" stop-color="#8e8e8e"/>
        </linearGradient>
        <linearGradient id="oliveBand" x1="0" y1="0" x2="0" y2="1">
          <stop offset="0" stop-color="#4f7a3a"/>
          <stop offset="1" stop-color="#7b9a4c"/>
        </linearGradient>
      </defs>
      <rect width="1000" height="570" fill="url(#silver)"/>
      <path d="M415 0 H545 C540 190 505 330 445 450 C472 320 470 150 415 0 Z" fill="url(#oliveBand)"/>
      <path d="M535 0 H565 C560 250 510 450 410 570 H378 C470 460 530 300 535 0 Z" fill="var(--swoosh-white)"/>
      <path d="M562 0 H1000 V570 H408 C505 455 555 260 562 0 Z" fill="var(--card-black)"/>
    </svg>

    <div class="brand-block">
      <span class="brand-scene" role="img" aria-label="Round brand illustration area in dark green night tones"></span>
      <p class="brand-name">Heron Creek Groves</p>
    </div>

    <div class="owners">
      <p>Dale Huston</p>
      <p>&amp;</p>
      <p>Annelise Vogt</p>
    </div>

    <ul class="contact-list">
      <li class="contact-item">
        <svg class="contact-icon" viewBox="0 0 24 24" aria-hidden="true"><path d="M6.6 10.8a15.1 15.1 0 0 0 6.6 6.6l2.2-2.2a1 1 0 0 1 1-.25 11.4 11.4 0 0 0 3.6.57 1 1 0 0 1 1 1V20a1 1 0 0 1-1 1A17 17 0 0 1 3 4a1 1 0 0 1 1-1h3.5a1 1 0 0 1 1 1c0 1.25.2 2.45.57 3.57a1 1 0 0 1-.25 1z"/></svg>
        <span>251-555-0148</span>
      </li>
      <li class="contact-item">
        <svg class="contact-icon" viewBox="0 0 24 24" aria-hidden="true"><path d="M2 6h20v12H2z"/><path d="M3.5 7.5 12 13l8.5-5.5" fill="none" stroke="#050505" stroke-width="1.5"/></svg>
        <span>info@heroncreekgroves.com</span>
      </li>
      <li class="contact-item">
        <svg class="contact-icon" viewBox="0 0 24 24" aria-hidden="true"><circle cx="12" cy="12" r="10"/><path d="M2 12h20M12 2c3 3 3 17 0 20M12 2c-3 3-3 17 0 20M4 7h16M4 17h16" fill="none" stroke="#050505" stroke-width="1.3"/></svg>
        <span>heroncreekgroves.com</span>
      </li>
      <li class="contact-item">
        <svg class="contact-icon" viewBox="0 0 24 24" aria-hidden="true"><path d="M12 3 2 12h3v9h5v-6h4v6h5v-9h3z"/></svg>
        <span class="address-lines"><span>31857 CR 46 Pinecrest,</span><span>AL 36541</span></span>
      </li>
    </ul>
  </div>
</body>
</html>
```